Tovrel Business Card

We are a modern retail clothing store. Established in 1994. I need a presentable card that will amaze vendors when given to them.

Front: Logo in middle
Info Side:

Name: Omar Latif
Cell: 212-555-0148
Work: 212-555-0192 EXT. 417
Email: Omar@tovrel.example
Website: www.Tovrel.example

Industry/Entity Type

Business

```html
<!DOCTYPE html>
<html lang="en">
<head>
<meta charset="utf-8">
<title>Tovrel Business Card</title>
<link rel="stylesheet" href="https://fonts.googleapis.com/css2?family=Arimo:wght@400;700&display=swap">
<style>
  :root {
    --backdrop: #2b2b2b;
    --card-black: #0b0b0b;
    --card-white: #ffffff;
    --text-white: #ffffff;
    --text-grey: #a8a8a8;
    --text-dark: #111111;
    --rule: #8a8a8a;
    --font: "Arimo", Arial, sans-serif;
  }
  * { box-sizing: border-box; margin: 0; padding: 0; }
  html, body {
    width: 1200px; height: 950px; overflow: hidden;
    background: var(--backdrop);
    font-family: var(--font);
  }
  .canvas { position: relative; width: 1200px; height: 950px; }
  .card {
    position: absolute; left: 250px; width: 700px; height: 400px;
    background: var(--card-black); overflow: hidden;
    box-shadow: 0 14px 40px rgba(0,0,0,.45);
  }
  .card--front { top: 50px; }
  .card--info { top: 500px; }

  /* Front */
  .front-name {
    position: absolute; left: 0; right: 0; top: 140px;
    text-align: center; color: var(--text-white);
    font-size: 78px; font-weight: 700; letter-spacing: 2px;
  }
  .front-web {
    position: absolute; left: 0; right: 0; top: 262px;
    display: flex; align-items: center; justify-content: center; gap: 18px;
    color: var(--text-grey); font-size: 15px; letter-spacing: 7px;
  }
  .front-web .rule { width: 90px; height: 1px; background: var(--rule); }

  /* Info side */
  .info-name {
    position: absolute; left: 0; right: 0; top: 50px;
    text-align: center; color: var(--text-white);
    font-size: 64px; font-weight: 700; letter-spacing: 2px;
  }
  .band {
    position: absolute; left: 0; top: 150px; width: 700px; height: 68px;
    background: var(--card-white);
  }
  .band-column {
    position: absolute; left: 610px; top: 150px; width: 90px; height: 250px;
    background: var(--card-white);
  }
  .person { position: absolute; left: 40px; top: 162px; color: var(--text-dark); }
  .person-name { font-size: 19px; font-weight: 700; letter-spacing: .5px; }
  .person-role { font-size: 13px; margin-top: 4px; letter-spacing: .5px; }

  .phones { position: absolute; left: 40px; top: 240px; color: var(--text-grey); font-size: 15px; }
  .contact-line { display: flex; align-items: center; gap: 10px; height: 26px; white-space: nowrap; }
  .contact-line svg { width: 14px; height: 14px; fill: var(--text-grey); flex: none; }

  .online { position: absolute; right: 110px; top: 318px; color: var(--text-grey); font-size: 15px; }
  .online .contact-line { justify-content: flex-end; }
</style>
</head>
<body>
<div class="canvas">

  <section class="card card--front" aria-label="Card front">
    <div class="front-name">Tovrel</div>
    <div class="front-web"><span class="rule"></span><span>www.tovrel.example</span><span class="rule"></span></div>
  </section>

  <section class="card card--info" aria-label="Card info side">
    <div class="info-name">Tovrel</div>
    <div class="band"></div>
    <div class="band-column"></div>

    <div class="person">
      <div class="person-name">OMAR LATIF</div>
      <div class="person-role">CEO/FOUNDER</div>
    </div>

    <div class="phones">
      <div class="contact-line">
        <svg viewBox="0 0 14 14" aria-hidden="true"><path d="M3 0h8a1 1 0 0 1 1 1v12a1 1 0 0 1-1 1H3a1 1 0 0 1-1-1V1a1 1 0 0 1 1-1zm1 2v8h6V2zm3 9a1 1 0 1 0 0 2 1 1 0 0 0 0-2z"/></svg>
        <span>212-555-0148</span>
      </div>
      <div class="contact-line">
        <svg viewBox="0 0 14 14" aria-hidden="true"><path d="M1 4c0-2 2-3 6-3s6 1 6 3v1h-3V4H4v1H1zm2 2h8l2 7H1zm4 1.5a2 2 0 1 0 0 4 2 2 0 0 0 0-4z"/></svg>
        <span>212-555-0192 EXT. 417</span>
      </div>
    </div>

    <div class="online">
      <div class="contact-line">
        <span>Omar@tovrel.example</span>
        <svg viewBox="0 0 14 14" aria-hidden="true"><path d="M0 3h14v8H0zm1 1v.4l6 3.6 6-3.6V4z"/></svg>
      </div>
      <div class="contact-line">
        <span>www.Tovrel.example</span>
        <svg viewBox="0 0 14 14" aria-hidden="true"><circle cx="7" cy="7" r="6"/><path d="M1 7h12M7 1c2.5 3 2.5 9 0 12M7 1c-2.5 3-2.5 9 0 12" stroke="#0b0b0b" stroke-width="1" fill="none"/></svg>
      </div>
    </div>
  </section>

</div>
</body>
</html>
```